Letterhead PT. Kencana Tirta Mandiri Developer

Alo , My Company need a letterhead design for PT. Kencana Tirta Mandiri developer Real Estate , i need your each other creative design letterhead for my PT.Kencana Tirta Mandiri Developer Real Estate guys
input my data in letterhead :
Address : Komp. Ruko Seroja Blok F No. 27
No. Telp : 0778 352 6147 / 0812 4539 1768
Email : kencanatirtamandiri@mailbox.example
Website : www.kencanatirtamandiri.example

Target Market(s)

Buyer Property Real Estate & Investor

Industry/Entity Type

Real Estate Development

Font styles to use
Serif
Sans Serif

Requirements
Must have
• according to your creative each other guys as long i need
• Address : Komp. Ruko Seroja Blok F No. 27
• No. Telp : 0778 352 6147 / 0812 4539 1768
• Email : kencanatirtamandiri@mailbox.example
• Website : www.kencanatirtamandiri.example
Nice to have
Should not have
• don't want another colour except : white , dark blue n gold suit to our logo developer real estate

```html
<!DOCTYPE html>
<html lang="en">
<head>
<meta charset="utf-8">
<title>PT. Kencana Tirta Mandiri Developer — Letterhead</title>
<link rel="stylesheet" href="https://fonts.googleapis.com/css2?family=Arimo:wght@400;700&family=Open+Sans:wght@600;700&display=swap">
<style>
  :root {
    --navy: #0f2c56;
    --gold: #d9962f;
    --bronze: #a9591f;
    --ink: #3a3a3a;
    --body-grey: #8a8a8a;
    --stage: #e4e4e4;
    --paper: #ffffff;
  }
  * { box-sizing: border-box; margin: 0; padding: 0; }
  html, body { width: 1200px; height: 795px; overflow: hidden; }
  body {
    background: var(--stage);
    font-family: "Arimo", Arial, sans-serif;
    position: relative;
  }
  .letterhead {
    position: absolute;
    left: 330px; top: 16px;
    width: 540px; height: 763px;
    background: var(--paper);
    box-shadow: 0 4px 18px rgba(0,0,0,.18);
    overflow: hidden;
  }
  .contact {
    position: absolute;
    top: 28px; right: 34px;
    width: 200px;
    font-size: 7.5px;
    line-height: 1.45;
    color: var(--navy);
  }
  .contact__company { font-weight: 700; }
  .contact__row { display: flex; align-items: center; gap: 4px; }
  .contact__icon {
    width: 9px; height: 9px; border-radius: 50%;
    background: var(--navy);
    display: inline-flex; align-items: center; justify-content: center;
    flex: none;
  }
  .brand {
    position: absolute;
    top: 96px; left: 40px;
    display: flex; align-items: center; gap: 8px;
  }
  .brand__mark { width: 14px; height: 14px; background: var(--navy); }
  .brand__name {
    font-family: "Open Sans", Arial, sans-serif;
    font-weight: 700;
    font-size: 13px;
    color: var(--navy);
    letter-spacing: .2px;
    text-transform: uppercase;
  }
  .letter {
    position: absolute;
    top: 160px; left: 40px; right: 44px;
    color: var(--ink);
    font-size: 10.5px;
    line-height: 1.3;
  }
  .letter__date { margin-bottom: 14px; }
  .letter__recipient { margin-bottom: 14px; }
  .letter__salutation { font-weight: 700; margin-bottom: 14px; font-size: 11px; }
  .letter__body p {
    color: var(--body-grey);
    font-size: 9.5px;
    line-height: 1.3;
    text-align: justify;
    margin-bottom: 13px;
  }
  .closing {
    margin-top: 10px;
    margin-left: auto;
    width: 130px;
    font-size: 9.5px;
    color: var(--ink);
    line-height: 1.3;
  }
  .closing__signature {
    width: 96px; height: 26px;
    margin: 6px 0 4px;
    background: linear-gradient(90deg, rgba(30,30,30,.06), rgba(30,30,30,.16), rgba(30,30,30,.06));
    border-radius: 3px;
  }
  .footer-bands {
    position: absolute;
    left: 0; right: 0; bottom: 0;
  }
  .footer-bands__gold { height: 4px; background: var(--gold); }
  .footer-bands__gap { height: 3px; background: var(--paper); }
  .footer-bands__navy { height: 14px; background: var(--navy); }
  .website {
    position: absolute;
    left: 40px; bottom: 40px;
    font-size: 10px;
    color: var(--bronze);
  }
</style>
</head>
<body>
  <main class="letterhead">
    <header>
      <div class="contact">
        <div class="contact__company">PT. Kencana Tirta Mandiri Developer</div>
        <div>Komp. Ruko Seroja Blok F No. 27</div>
        <div class="contact__row">
          <span class="contact__icon">
            <svg width="6" height="6" viewBox="0 0 10 10"><path d="M2 1 L4 1 L4.8 3.2 L3.6 4.2 Q4.6 6 6 6.6 L7 5.4 L9 6.2 L9 8.2 Q8.6 9 7.6 9 Q1 8.4 1 2 Q1 1 2 1Z" fill="#fff"/></svg>
          </span>
          0778 352 6147 / 0812 4539 1768
        </div>
        <div class="contact__row">
          <span class="contact__icon">
            <svg width="6" height="6" viewBox="0 0 10 10"><rect x="1" y="2.5" width="8" height="5.5" fill="none" stroke="#fff" stroke-width="1.2"/><path d="M1 2.5 L5 5.8 L9 2.5" fill="none" stroke="#fff" stroke-width="1.2"/></svg>
          </span>
          kencanatirtamandiri@mailbox.example
        </div>
      </div>
      <div class="brand">
        <span class="brand__mark"></span>
        <span class="brand__name">PT. Kencana Tirta Mandiri</span>
      </div>
    </header>

    <section class="letter">
      <p class="letter__date">January 12, 2014</p>
      <div class="letter__recipient">
        <div>Mr. Daniel Marlow</div>
        <div>President</div>
        <div>Nusa Prima Corporation</div>
        <div>111 Street Name, Suite#</div>
        <div>City, State, 12345</div>
      </div>
      <p class="letter__salutation">Dear Mr. Daniel,</p>
      <div class="letter__body">
        <p>Lorem Ipsum is simply dummy text of the printing and typesetting industry. Lorem Ipsum has been the industry's standard dummy text ever since the 1500s, when an unknown printer took a galley of type and scrambled it to make a type specimen book. It has survived not only five centuries, but also the leap into electronic typesetting, remaining essentially unchanged.</p>
        <p>The standard chunk of Lorem Ipsum used since the 1500s is reproduced below for those interested. Sections 1.10.32 and 1.10.33 from "de Finibus Bonorum et Malorum" by Cicero are also reproduced in their exact original form, accompanied by English versions from the 1914 translation by H. Rackham.</p>
        <p>Lorem Ipsum is simply dummy text of the printing and typesetting industry. Lorem Ipsum has been the industry's standard dummy text ever since the 1500s, when an unknown printer took a galley of type and scrambled it to make a type specimen book. It has survived not only five centuries, but also the leap into electronic typesetting, remaining essentially unchanged. It was popularised in the</p>
      </div>
      <div class="closing">
        <div>Sincerely Your,</div>
        <div class="closing__signature" role="img" aria-label="Handwritten signature"></div>
        <div>Name Last Name</div>
        <div>Company Name</div>
      </div>
    </section>

    <footer>
      <div class="website">www.kencanatirtamandiri.example</div>
      <div class="footer-bands" aria-hidden="true">
        <div class="footer-bands__gold"></div>
        <div class="footer-bands__gap"></div>
        <div class="footer-bands__navy"></div>
      </div>
    </footer>
  </main>
</body>
</html>
```